Cleaning Company Banner

Looking to have a Banner made that shows our contact information and shows what we do with good imagery to catch cars driving by. Will be a 6' x 3' banner (landscape). Attached our logo and flyer that we currently hand out.

```html
<!DOCTYPE html>
<html lang="en">
<head>
<meta charset="utf-8">
<title>BrightMark Cleaning Banner</title>
<link href="https://fonts.googleapis.com/css2?family=Poppins:ital,wght@0,400;0,600;0,700;0,800;1,400&display=swap" rel="stylesheet">
<style>
  :root {
    --page-bg: #e9ecef;
    --sky-light: #eef4f9;
    --sky-mid: #dce8f2;
    --brand-blue: #1a78c2;
    --brand-blue-deep: #1362a8;
    --navy: #0b4a85;
    --navy-dark: #083a6b;
    --teal: #1fa58f;
    --teal-light: #5cc7b5;
    --gold: #e0b21a;
    --ink: #1b1b1b;
    --white: #ffffff;
  }
  * { margin: 0; padding: 0; box-sizing: border-box; }
  html, body {
    width: 1200px;
    height: 1117px;
    overflow: hidden;
    background: var(--page-bg);
  }
  .canvas {
    width: 1200px;
    height: 1117px;
    display: flex;
    align-items: center;
    justify-content: center;
  }
  .banner {
    width: 1120px;
    height: 576px;
    display: block;
    box-shadow: 0 10px 30px rgba(0,0,0,0.18);
  }
  .brand-name { font-family: 'Poppins', sans-serif; font-weight: 600; fill: var(--teal); }
  .services-title { font-family: 'Poppins', sans-serif; font-weight: 700; fill: var(--white); }
  .service-label { font-family: 'Poppins', sans-serif; font-weight: 400; fill: var(--ink); }
  .headline {
    font-family: 'Poppins', sans-serif;
    font-weight: 800;
    fill: var(--white);
    letter-spacing: 0.5px;
  }
  .owner-name { font-family: 'Poppins', sans-serif; font-weight: 700; fill: var(--gold); }
  .owner-role { font-family: 'Poppins', sans-serif; font-weight: 400; font-style: italic; fill: var(--gold); }
  .contact-text { font-family: 'Poppins', sans-serif; font-weight: 400; fill: var(--white); }
  .icon-disc { fill: var(--brand-blue); }
  .icon-line { fill: none; stroke: var(--white); stroke-width: 2.4; stroke-linecap: round; stroke-linejoin: round; }
</style>
</head>
<body>
<main class="canvas">
  <svg class="banner" viewBox="0 0 1634 840" xmlns="http://www.w3.org/2000/svg" aria-label="BrightMark Cleaning banner">
    <defs>
      <linearGradient id="bg-sky" x1="0" y1="0" x2="1" y2="1">
        <stop offset="0" stop-color="var(--sky-light)"/>
        <stop offset="1" stop-color="var(--sky-mid)"/>
      </linearGradient>
      <linearGradient id="photo-tones" x1="0" y1="0" x2="1" y2="0">
        <stop offset="0" stop-color="#7fbf5a"/>
        <stop offset="0.25" stop-color="#5a9fd0"/>
        <stop offset="0.5" stop-color="#c9d3da"/>
        <stop offset="0.8" stop-color="#dfe4e8"/>
        <stop offset="1" stop-color="#8fae8a"/>
      </linearGradient>
      <linearGradient id="blue-field" x1="0" y1="0" x2="0" y2="1">
        <stop offset="0" stop-color="var(--brand-blue)"/>
        <stop offset="1" stop-color="var(--brand-blue-deep)"/>
      </linearGradient>
      <linearGradient id="teal-band" x1="0" y1="0" x2="1" y2="0">
        <stop offset="0" stop-color="var(--teal)"/>
        <stop offset="0.5" stop-color="var(--teal-light)"/>
        <stop offset="1" stop-color="var(--teal)"/>
      </linearGradient>
      <filter id="text-lift" x="-5%" y="-20%" width="110%" height="140%">
        <feDropShadow dx="2" dy="3" stdDeviation="2" flood-color="#06305a" flood-opacity="0.6"/>
      </filter>
    </defs>

    <!-- base -->
    <rect class="banner-bg" width="1634" height="840" fill="url(#bg-sky)"/>

    <!-- photo area -->
    <g role="img" aria-label="Photo of cleaning supplies in a basket and a cleaning crew wiping desks in a bright office">
      <path d="M455,0 H1634 V470 C1560,395 1400,345 1150,345 C950,345 790,332 650,325 C560,300 480,150 455,0 Z" fill="url(#photo-tones)"/>
    </g>

    <!-- white rim between photo and blue field -->
    <path d="M640,322 C800,332 950,340 1150,340 C1400,340 1560,390 1634,465 V480 C1560,405 1400,355 1150,355 C950,355 800,345 650,338 Z" fill="var(--white)"/>

    <!-- blue message field -->
    <path d="M650,338 C800,345 950,355 1150,355 C1400,355 1560,405 1634,480 V840 H700 C640,760 600,620 610,500 C615,420 630,370 650,338 Z" fill="url(#blue-field)"/>

    <!-- bottom waves -->
    <path d="M0,745 C250,820 480,800 700,740 C950,660 1250,560 1634,640 V840 H0 Z" fill="url(#teal-band)"/>
    <path d="M0,768 C250,838 480,822 700,762 C950,684 1250,590 1634,666 V840 H0 Z" fill="var(--navy-dark)"/>
    <path d="M0,780 C250,848 480,834 700,774 C950,698 1250,606 1634,680 V840 H0 Z" fill="var(--navy)"/>

    <!-- brand name -->
    <g class="brand">
      <circle cx="250" cy="95" r="44" fill="var(--teal)"/>
      <text class="brand-name" x="250" y="248" text-anchor="middle" font-size="66" letter-spacing="2">BRIGHTMARK</text>
      <text class="brand-name" x="250" y="296" text-anchor="middle" font-size="30" letter-spacing="6">CLEANING</text>
    </g>

    <!-- services -->
    <g class="services">
      <path d="M0,342 H532 A38,38 0 0 1 570,380 A38,38 0 0 1 532,418 H0 Z" fill="var(--navy)"/>
      <text class="services-title" x="280" y="398" text-anchor="middle" font-size="50">Our Services</text>

      <g class="service-item">
        <circle class="icon-disc" cx="103" cy="475" r="31"/>
        <path class="icon-line" d="M92,463 h10 v6 l4,4 v16 h-18 v-16 l4,-4 z M108,481 h10 v8 h-10"/>
        <text class="service-label" x="163" y="486" font-size="34">Residential Cleaning</text>
      </g>
      <g class="service-item">
        <circle class="icon-disc" cx="103" cy="545" r="31"/>
        <path class="icon-line" d="M88,540 h16 l-2,18 h-12 z M112,528 v26 M106,558 h12 l-2,-6 h-8 z"/>
        <text class="service-label" x="163" y="556" font-size="34">Commercial Cleaning</text>
      </g>
      <g class="service-item">
        <circle class="icon-disc" cx="103" cy="613" r="31"/>
        <path class="icon-line" d="M90,600 h14 l-4,6 v22 h-12 v-20 z M94,617 v8 M90,621 h8 M108,600 l6,-3 M108,605 l7,0"/>
        <text class="service-label" x="163" y="624" font-size="34">Construction Cleaning</text>
      </g>
      <g class="service-item">
        <circle class="icon-disc" cx="103" cy="686" r="31"/>
        <path class="icon-line" d="M92,700 l8,-22 l6,4 l-4,18 z M108,676 h8 v24 h-10 M112,672 v4"/>
        <text class="service-label" x="163" y="698" font-size="34">Antiviral Disinfection</text>
      </g>
    </g>

    <!-- headline -->
    <g class="headline-block" filter="url(#text-lift)">
      <text class="headline" x="1118" y="447" text-anchor="middle" font-size="51">QUALITY DRIVEN AND</text>
      <text class="headline" x="1118" y="503" text-anchor="middle" font-size="51">RELIABLE TO TAKE CARE OF ALL</text>
      <text class="headline" x="1118" y="559" text-anchor="middle" font-size="51">YOUR CLEANING NEEDS!!!</text>
    </g>

    <!-- contact -->
    <g class="contact">
      <text x="1553" y="743" text-anchor="end"><tspan class="owner-name" font-size="40">Dana Whitfield</tspan><tspan class="owner-role" font-size="27" dx="10">(Owner/Operator)</tspan></text>

      <circle cx="738" cy="778" r="15" fill="var(--white)"/>
      <path d="M731,771 c1,-2 3,-2 4,0 l1,3 c0,1 -1,2 -2,3 c1,3 3,5 6,6 c1,-1 2,-2 3,-2 l3,1 c2,1 2,3 0,4 c-2,2 -5,2 -8,0 c-4,-2 -7,-6 -8,-9 c-1,-2 -1,-4 1,-6 z" fill="var(--navy)"/>
      <text class="contact-text" x="760" y="790" font-size="33">(555) 014-2297</text>

      <circle cx="1060" cy="778" r="15" fill="var(--white)"/>
      <rect x="1051" y="771" width="18" height="13" rx="1.5" fill="none" stroke="var(--navy)" stroke-width="2"/>
      <path d="M1051,772 l9,7 l9,-7" fill="none" stroke="var(--navy)" stroke-width="2"/>
      <text class="contact-text" x="1082" y="790" font-size="33">hello@brightmarkclean.com</text>
    </g>
  </svg>
</main>
</body>
</html>
```